Professional, polished website design for boutique wealth management firm

Hello, thank you for your interest. PLEASE READ THE BRIEF BEFORE SUBMITTING THE DESIGN.-
PLEASE USE THE ATTACHED HOME PAGE COPY FOR THIS DESIGN.
We are looking for a professional, polished design that helps portray trust and credibility for a well-established independent wealth management firm. We have copy we've written for the home page and we'd like the design and imagery to play up the copy, so there's a better chance someone will read it all. So the headlines etc should all be easy to read and the design should draw the eye towards them. For colors, again trust is important so probably blue as a dominant color, but you can also use gray, green, etc. We'd like to avoid too much use of the color red (due to financial, association with loss). SO PLEASE AVOID USE OF THE COLOR RED. We also like bright orange or yellow for call to action buttons.

Please keep the design EASY TO MAINTAIN in wordpress as well.

I have attached home page copy as well as logo files.

Here's some sites that we like so feel free to use as inspiration:
https://www.brovaltcapitalworks.example/, https://harborpathpensionsplains.example/
https://tavrin-oakes.example/, https://plantfornextyear.example/, https://ferngatefinancial.example/

As another option/idea, I like the idea of a simple format with a clean image similar to this for the home page: https://www.pixmeadowstock.example/detail/photo/calculator-falling-royalty-free-image/31684207?adppopup=true
Just an idea.

Also please be sure to incorporate the QWA /Accredited Wealth Steward logo as well, farther down the page is fine.

Thank you for your help! Feel free to contact me with any questions.

Target Market(s)

Individuals aged 48-62 who are looking to maximize their wealth, such as business owners, executives, engineers, successful tradespeople, etc.

Industry/Entity Type

Finance--wealth management

Font styles to use
Sans Serif

Requirements
Must have
• Professional and polished, Call to action buttons must be clear and stand out, headlines must be clear and stand out, also text must be big enough to be easily readable by most people
Should not have
• Anything casual, frilly, etc.

```html
<!DOCTYPE html>
<html lang="en">
<head>
<meta charset="utf-8">
<title>Keystone Harbor Advisors</title>
<link href="https://fonts.googleapis.com/css2?family=Libre+Baskerville:wght@400;700&family=Outfit:wght@300;400;500;600&display=swap" rel="stylesheet">
<style>
:root{
  --navy:#2a3590;
  --navy-dark:#1d2540;
  --orange:#fdac00;
  --ink:#1f2233;
  --text:#444a5c;
  --muted:#8b90a0;
  --soft:#f4f4f9;
  --soft2:#eeeef6;
  --line:#d9dbe3;
  --green:#7cc242;
  --white:#ffffff;
}
*{box-sizing:border-box;margin:0;padding:0}
html,body{width:1200px;height:3881px;overflow:hidden}
body{font-family:"Outfit",sans-serif;color:var(--ink);background:var(--white);position:relative}
.abs{position:absolute}
.brand{display:flex;align-items:center;gap:10px}
.brand-dot{width:30px;height:30px;border-radius:50%;background:var(--navy)}
.brand-name{font-family:"Outfit",sans-serif;font-weight:500;color:var(--navy);font-size:20px;letter-spacing:.5px}
/* header */
.site-header{left:0;top:0;width:1200px;height:78px;background:var(--white)}
.site-header .brand{position:absolute;left:118px;top:24px}
.nav{position:absolute;left:460px;top:36px;display:flex;gap:22px;font-family:"Libre Baskerville",serif;font-size:11.5px;color:var(--ink)}
.btn-outline-sm{position:absolute;left:796px;top:26px;width:124px;height:34px;border:1px solid #9a9ca8;border-radius:17px;font-family:"Libre Baskerville",serif;font-size:11px;display:flex;align-items:center;justify-content:center}
.btn-cta-sm{position:absolute;left:929px;top:26px;width:152px;height:34px;background:var(--orange);border-radius:17px;color:#fff;font-family:"Libre Baskerville",serif;font-weight:700;font-size:11px;display:flex;align-items:center;justify-content:center}
/* hero */
.hero{left:0;top:78px;width:1200px;height:549px;background:linear-gradient(90deg,#eceef5,#e3e5ee 60%,#eef0f6)}
.hero-title{left:193px;top:170px;font-family:"Libre Baskerville",serif;font-size:26px;line-height:40px;color:var(--ink);letter-spacing:-.3px}
.hero-title b{font-weight:700}
.btn-navy{background:var(--navy);color:#fff;border-radius:22px;display:flex;align-items:center;justify-content:center}
.hero .btn-navy{left:193px;top:314px;width:152px;height:42px;font-family:"Libre Baskerville",serif;font-size:14px}
.hero-photo{left:577px;top:88px;width:534px;height:352px;background:#fff;padding:7px;box-shadow:0 6px 20px rgba(0,0,0,.15)}
.hero-photo div{width:100%;height:100%;background:linear-gradient(135deg,#3d4a60,#8a7c6a 55%,#c9c2b4)}
.hero-badge{left:542px;top:368px;width:106px;height:106px;border-radius:50%;background:#fff;box-shadow:0 4px 14px rgba(0,0,0,.12);display:flex;align-items:center;justify-content:center}
/* intro */
.intro-h{left:193px;top:742px;font-size:25px;line-height:34px;font-weight:500;width:380px;color:var(--ink)}
.intro-p{left:193px;top:864px;width:370px;font-size:12.5px;line-height:21px;color:var(--text)}
.btn-pill{border:1.5px solid #9a9ca8;border-radius:20px;display:flex;align-items:center;justify-content:center;font-size:12.5px;font-weight:500;background:#fff;color:var(--ink)}
.intro .btn-pill{left:193px;top:957px;width:204px;height:37px}
.intro-circle-l{left:-110px;top:700px;width:200px;height:330px;border-radius:50%;background:var(--soft)}
.intro-circle-r{left:785px;top:695px;width:365px;height:365px;border-radius:50%;background:var(--soft2)}
.intro-art{left:720px;top:695px;width:300px;height:370px;border-radius:48% 52% 40% 60%;background:linear-gradient(160deg,#5a63c9,#2a3590)}
/* difference */
.diff{left:0;top:1134px;width:1200px;height:464px;background:var(--soft)}
.diff-band{left:0;top:1134px;width:396px;height:464px;background:var(--orange)}
.diff-photo{left:196px;top:1218px;width:320px;height:294px;background:linear-gradient(135deg,#e8edf2,#a8b4c2 60%,#2b3346);box-shadow:0 4px 14px rgba(0,0,0,.15)}
.diff-h{left:590px;top:1224px;width:410px;font-size:21.5px;line-height:34px;font-weight:500}
.diff-p{left:590px;top:1340px;width:400px;font-size:12.5px;line-height:20.5px;color:var(--text)}
.diff .btn-pill,.diff-btn{left:590px;top:1470px;width:176px;height:35px}
/* strategies */
.strat{left:0;top:1598px;width:1200px;height:480px;background:linear-gradient(100deg,#4a4b50,#5f5f63 50%,#49494d)}
.strat-l1{left:0;top:1728px;width:1200px;text-align:center;color:#fff;font-size:26px;font-weight:300}
.strat-l2{left:0;top:1767px;width:1200px;text-align:center;color:#fff;font-size:26px;font-weight:500}
.strat-p{left:0;top:1821px;width:1200px;text-align:center;color:#fff;font-size:13.5px}
.strat-btn{left:533px;top:1867px;width:134px;height:34px;background:#fff;border-radius:17px;font-size:12.5px;font-weight:500;display:flex;align-items:center;justify-content:center}
/* services */
.svc-bg{left:0;top:2078px;width:1200px;height:450px;background:#f6f6fa}
.svc-panel{left:641px;top:2035px;width:559px;height:392px;background:var(--soft2)}
.svc-h{left:192px;top:2150px;font-size:38px;line-height:42px;color:var(--ink)}
.svc-h b{font-weight:600}
.svc-h span{font-weight:400;font-size:33px}
.svc-item{width:341px;height:68px;background:#fff;box-shadow:0 2px 8px rgba(0,0,0,.05);display:flex;align-items:center;gap:20px;padding-left:18px;font-size:16.5px;line-height:22px}
.svc-num{width:38px;height:38px;border-radius:50%;background:var(--orange);color:#fff;font-size:14px;display:flex;align-items:center;justify-content:center;flex:none}
/* checkup */
.check-photo{left:381px;top:2528px;width:624px;height:416px;background:linear-gradient(135deg,#cfd6e6,#eef0f6 45%,#9aa6c6)}
.check-box{left:193px;top:2548px;width:427px;height:378px;background:var(--navy);clip-path:polygon(0 0,100% 6%,100% 92%,0 100%)}
.check-h{left:258px;top:2620px;color:#fff;font-size:22px;line-height:33px;font-weight:500}
.check-p{left:258px;top:2697px;width:300px;color:#fff;font-size:10.5px;line-height:18px}
.check-btn{left:258px;top:2823px;width:115px;height:32px;background:#fff;border-radius:16px;font-size:11.5px;font-weight:500;display:flex;align-items:center;justify-content:center}
/* contact */
.contact-dot{left:575px;top:3033px;width:50px;height:50px;border-radius:50%;background:var(--navy)}
.contact-h{left:0;top:3108px;width:1200px;text-align:center;font-size:32px;font-weight:600;letter-spacing:1px}
.contact-p{left:0;top:3152px;width:1200px;text-align:center;font-size:13.5px;line-height:20px;color:var(--text)}
.footer-bg{left:0;top:3330px;width:1200px;height:551px}
.form-card{left:193px;top:3216px;width:812px;height:302px;background:#fff;border-top:3px solid var(--green);box-shadow:0 6px 24px rgba(0,0,0,.12)}
.form-title{position:absolute;left:90px;top:30px;font-size:18px;color:var(--ink)}
.field{position:absolute;height:32px;border:1px solid var(--line);font-size:10px;color:var(--muted);padding:9px 14px}
.submit{position:absolute;left:90px;top:241px;width:116px;height:32px;background:var(--navy);color:#fff;font-size:12px;font-weight:600;display:flex;align-items:center;justify-content:center}
/* footer */
.footer .brand{position:absolute;left:193px;top:3590px}
.footer .brand-name{color:#fff;font-size:24px}
.footer .brand-dot{background:#fff;width:40px;height:40px}
.foot-about{left:193px;top:3678px;width:280px;color:#e6e8ef;font-size:9.5px;line-height:16px}
.foot-h{color:#fff;font-size:12px;font-weight:600;padding-bottom:8px;border-bottom:1px solid rgba(255,255,255,.25);width:160px}
.foot-links{list-style:none;color:#e6e8ef;font-size:11px;line-height:19px;margin-top:10px}
.sub-row{display:flex;margin-top:8px}
.sub-row span{width:108px;height:24px;background:#fff}
.sub-row b{width:70px;height:24px;background:var(--orange);color:#fff;font-weight:400;font-size:10px;display:flex;align-items:center;justify-content:center}
.socials{display:flex;gap:6px;margin-top:12px}
.socials i{width:20px;height:20px;border:1px solid #fff;border-radius:50%}
.foot-rule{left:193px;top:3812px;width:812px;height:1px;background:rgba(255,255,255,.25)}
.foot-copy{left:193px;top:3838px;color:#fff;font-size:10.5px}
.foot-legal{left:836px;top:3838px;color:#fff;font-size:10.5px;width:170px;text-align:right}
</style>
</head>
<body>

<header class="abs site-header">
  <div class="brand"><span class="brand-dot"></span><span class="brand-name">KEYSTONE HARBOR</span></div>
  <nav class="nav"><span>WHO WE ARE</span><span>SERVICES</span><span>NEWS</span><span>CONTACT</span></nav>
  <div class="btn-outline-sm">CLIENT LOGIN</div>
  <div class="btn-cta-sm">GET FREE QUOTE</div>
</header>

<section class="abs hero">
  <h1 class="abs hero-title" style="top:170px">THE MOST EFFECTIVE<br><b>FINANCIAL PLANS</b> START<br>WITH TAX PLANNING.</h1>
  <div class="abs btn-navy">LEARN MORE</div>
  <div class="abs hero-photo" role="img" aria-label="Photo of an advisor working a calculator over tax documents"><div></div></div>
  <div class="abs hero-badge"><span class="brand-dot" style="width:54px;height:54px;border-radius:50%;background:var(--navy)"></span></div>
</section>

<section class="intro">
  <div class="abs intro-circle-l"></div>
  <div class="abs intro-circle-r"></div>
  <div class="abs intro-art" role="img" aria-label="Decorative blue illustration with a calculator and stars"></div>
  <h2 class="abs intro-h">Few financial advisors offer tax expertise, but when they do, you benefit.</h2>
  <p class="abs intro-p">Learn how our unique team combines financial planning, investments and smart tax and income generation strategies to help you achieve your goals faster.</p>
  <div class="abs btn-pill">Learn why we're different</div>
</section>

<section class="diff">
  <div class="abs diff"></div>
  <div class="abs diff-band"></div>
  <div class="abs diff-photo" role="img" aria-label="Photo of a smiling financial specialist holding documents"></div>
  <h2 class="abs diff-h">Cookie-cutter financial planning and investment can leave your future at risk. That's why we do it differently.</h2>
  <p class="abs diff-p">You need better strategies in today's complex financial landscape. At Keystone Harbor Advisors, we bring financial planning, investment management, retirement income, tax and estate planning expertise together under one roof. Our unique team works together to help you make the most of your resources.</p>
  <div class="abs btn-pill diff-btn">Meet Our Specialists</div>
</section>

<section>
  <div class="abs strat" role="img" aria-label="Dimmed photo of an advisor reviewing figures at a desk"></div>
  <p class="abs strat-l1">Better strategies to preserve and grow wealth,</p>
  <p class="abs strat-l2">Generate income and reduce your taxes.</p>
  <p class="abs strat-p">Here's what you can expect when you work with Keystone.</p>
  <div class="abs strat-btn">Get a Quote</div>
</section>

<section>
  <div class="abs svc-bg"></div>
  <div class="abs svc-panel"></div>
  <h2 class="abs svc-h"><b>Personalized solutions</b><br><span>to help your money work<br>harder for you</span></h2>
  <div class="abs svc-item" style="left:193px;top:2317px"><span class="svc-num">1</span>Investment Management</div>
  <div class="abs svc-item" style="left:688px;top:2077px"><span class="svc-num">2</span>Comprehensive<br>Financial Planning</div>
  <div class="abs svc-item" style="left:688px;top:2157px"><span class="svc-num">3</span>Retirement Income Planning</div>
  <div class="abs svc-item" style="left:688px;top:2237px"><span class="svc-num">4</span>Tax Planning</div>
  <div class="abs svc-item" style="left:688px;top:2317px"><span class="svc-num">5</span>Estate Planning</div>
</section>

<section>
  <div class="abs check-photo" role="img" aria-label="Photo of hands with a pen and calculator over rising bar charts"></div>
  <div class="abs check-box"></div>
  <h2 class="abs check-h">The Keystone $549<br>Retirement Check-Up</h2>
  <p class="abs check-p">We know it's a big decision to hire or switch advisors. That's why we provide an easy way to try us out. At the same time, you can get a valuable second opinion to find out if you're on track to retire. There's no pressure, and either way, you'll walk away with valuable insights on what you should be doing to secure your future.</p>
  <div class="abs check-btn">Learn More</div>
</section>

<svg class="abs footer-bg" viewBox="0 0 1200 551" preserveAspectRatio="none">
  <defs><linearGradient id="footGrad" x1="0" y1="0" x2="0" y2="1"><stop offset="0" stop-color="#232c48"/><stop offset="1" stop-color="#151a2c"/></linearGradient></defs>
  <path d="M0 70 Q600 0 1200 70 L1200 551 L0 551 Z" fill="url(#footGrad)"/>
</svg>

<section>
  <div class="abs contact-dot"></div>
  <h2 class="abs contact-h">CONTACT</h2>
  <p class="abs contact-p">Lorem ipsum dolor sit amet, consectetur adipiscing elit<br>Nunc ac consectetur leo. Mauris aliquam.</p>
  <form class="abs form-card">
    <p class="form-title">Feel Free to Contact Us</p>
    <div class="field" style="left:90px;top:60px;width:310px">First Name</div>
    <div class="field" style="left:413px;top:60px;width:310px">Last Name</div>
    <div class="field" style="left:90px;top:104px;width:310px">Email</div>
    <div class="field" style="left:413px;top:104px;width:310px">Subject</div>
    <div class="field" style="left:90px;top:148px;width:633px;height:74px">Message...</div>
    <div class="submit">SUBMIT</div>
  </form>
</section>

<footer class="footer">
  <div class="brand"><span class="brand-dot"></span><span class="brand-name">KEYSTONE HARBOR</span></div>
  <p class="abs foot-about">With over 55 years of combined experience, Keystone Harbor Advisors helps successful people more effectively prepare for the future. Our unique small team of wealth managers, financial planners and tax professionals bring you the strategies you need to preserve your wealth, minimize your taxes and create a confident retirement. While we're based in Alder County, Ohio, we serve clients nationwide.</p>
  <div class="abs" style="left:576px;top:3594px">
    <p class="foot-h">SITELINKS</p>
    <ul class="foot-links"><li>Who We Are</li><li>Services</li><li>News</li><li>Sitemap</li><li>Client Login</li><li>Contact</li></ul>
  </div>
  <div class="abs" style="left:827px;top:3594px">
    <p class="foot-h" style="width:178px">STAY IN TOUCH</p>
    <p style="color:#e6e8ef;font-size:11px;margin-top:10px">Subscribe Our Newsletter</p>
    <div class="sub-row"><span></span><b>Subscribe</b></div>
    <div class="socials"><i></i><i></i><i></i></div>
  </div>
  <div class="abs foot-rule"></div>
  <p class="abs foot-copy">© 2021 Keystone Harbor Advisors. All Rights Reserved.</p>
  <p class="abs foot-legal">Privace &amp; Policy &nbsp;|&nbsp; Faq &nbsp;|&nbsp; Terms.</p>
</footer>

</body>
</html>
```